Snapframe Party Rentals New Business Card*

Need a business card designed for a Photo Booth Hire company.Must look very professional and colorful.A new creative logo would be a bonus. Our current logo is attached on here.

Contact Information for Business Card

Business Name: SNAPFRAME PARTY RENTALS
Contact Person: MARCUS OKAFOR
Mobile: 0491826350
Email: INFO@SNAPFRAMERENTALS.EXAMPLE
Website: WWW.SNAPFRAMERENTALS.EXAMPLE
social.example: SOCIAL.EXAMPLE/SNAPFRAME.PARTY.RNT

Font styles to use
Serif
Sans Serif
Script

Colors

Designer to choose colors to be used in the design.

Requirements
Must have
• Bonus if the colors match our website.

```html
<!DOCTYPE html>
<html lang="en">
<head>
<meta charset="utf-8">
<title>Snapframe Party Rentals – Business Card</title>
<link rel="stylesheet" href="https://fonts.googleapis.com/css2?family=Roboto:wght@300;400;500;700&display=swap">
<style>
  :root {
    --brand-blue: #2196ba;
    --accent-orange: #f26b21;
    --ink-grey: #555a5e;
    --rule-grey: #dcdcdc;
    --paper: #ffffff;
    --canvas: #ffffff;
  }
  html, body {
    margin: 0;
    width: 1200px;
    height: 1200px;
    overflow: hidden;
    background: var(--canvas);
    font-family: "Roboto", Arial, sans-serif;
  }
  .stage { position: relative; width: 1200px; height: 1200px; }
  .card {
    position: absolute;
    top: 218px;
    width: 437px;
    height: 763px;
    box-shadow: 2px 3px 6px rgba(0,0,0,0.28);
  }
  .card--front { left: 134px; background: var(--brand-blue); }
  .card--back { left: 630px; background: var(--paper); }

  .front-name {
    position: absolute;
    left: 0; right: 0;
    top: 140px;
    text-align: center;
    color: var(--paper);
    font-weight: 500;
    font-size: 56px;
    line-height: 1.12;
    letter-spacing: 1px;
    margin: 0;
  }
  .front-web {
    position: absolute;
    left: 0; right: 0;
    top: 616px;
    margin: 0;
    text-align: center;
    color: var(--paper);
    font-weight: 300;
    font-size: 23px;
  }

  .contact-name {
    position: absolute;
    left: 72px; top: 56px;
    margin: 0;
    color: var(--accent-orange);
    font-weight: 700;
    font-size: 27px;
    letter-spacing: 1px;
    line-height: 1;
  }
  .contact-role {
    position: absolute;
    left: 72px; top: 86px;
    margin: 0;
    color: var(--ink-grey);
    font-weight: 400;
    font-size: 26px;
    line-height: 1.1;
  }
  .contact-list {
    position: absolute;
    left: 40px; top: 140px;
    margin: 0; padding: 0;
    list-style: none;
  }
  .contact-item {
    display: flex;
    align-items: center;
    height: 36px;
    margin-bottom: 2px;
    color: var(--ink-grey);
    font-weight: 300;
    font-size: 21px;
  }
  .contact-icon { width: 22px; height: 22px; margin-right: 10px; flex: none; }
  .divider {
    position: absolute;
    left: 42px; top: 288px;
    width: 358px; height: 1px;
    background: var(--rule-grey);
  }
  .brand-mark {
    position: absolute;
    left: 168px; top: 378px;
    width: 100px; height: 100px;
    border-radius: 50%;
    background: var(--brand-blue);
  }
  .brand-name {
    position: absolute;
    left: 0; right: 0; top: 502px;
    margin: 0;
    text-align: center;
    color: var(--brand-blue);
    font-weight: 500;
    font-size: 44px;
    line-height: 1.12;
  }
</style>
</head>
<body>
<main class="stage">
  <section class="card card--front">
    <h1 class="front-name">SNAPFRAME<br>PARTY<br>RENTALS</h1>
    <p class="front-web">www.snapframerentals.example</p>
  </section>

  <section class="card card--back">
    <h2 class="contact-name">MARCUS OKAFOR</h2>
    <p class="contact-role">Contact Person</p>
    <ul class="contact-list">
      <li class="contact-item">
        <svg class="contact-icon" viewBox="0 0 24 24" aria-hidden="true">
          <rect x="1" y="5" width="22" height="15" rx="2" fill="var(--brand-blue)"/>
          <path d="M2 6 L12 13 L22 6" fill="none" stroke="#fff" stroke-width="2"/>
        </svg>
        info@snapframerentals.example
      </li>
      <li class="contact-item">
        <svg class="contact-icon" viewBox="0 0 24 24" aria-hidden="true">
          <path d="M6.6 10.8a15.1 15.1 0 0 0 6.6 6.6l2.2-2.2a1 1 0 0 1 1-.25 11.4 11.4 0 0 0 3.6.57 1 1 0 0 1 1 1V20a1 1 0 0 1-1 1A17 17 0 0 1 3 4a1 1 0 0 1 1-1h3.5a1 1 0 0 1 1 1c0 1.25.2 2.45.57 3.57a1 1 0 0 1-.25 1z" fill="var(--brand-blue)" transform="translate(24 0) scale(-1 1)"/>
        </svg>
        0491826350
      </li>
      <li class="contact-item">
        <svg class="contact-icon" viewBox="0 0 24 24" aria-hidden="true">
          <rect x="2" y="2" width="20" height="20" rx="3" fill="var(--brand-blue)"/>
        </svg>
        social.example/snapframe.party.rnt
      </li>
    </ul>
    <div class="divider"></div>
    <div class="brand-mark" aria-hidden="true"></div>
    <p class="brand-name">Snapframe<br>Party Rentals</p>
  </section>
</main>
</body>
</html>
```